Grand Opening / Live Music Event

My band is playing a Grand Opening event on Saturday April 5th. I need a flyer utilizing the attached image of our bass player and incorporating our band logo. This picture makes me laugh and gives the impression he is angry - like saying "it's going to be a celebration fool!" or something along those lines. I need to the flyer to pop and present an image that it will be an excellent party. Feel free to incorporate any background or theme style. You can find other images of my band in the event they are needed at: https://www.velorumhub.example/Corkvalleyband

Some details:

The event will be at Quimby's Hall. 8241 Larkspur Ave. #204, Frisco, Texas. (214) 705-9183 for table reservations.

Saturday April 5th. Party starts at 7:00 PM with an acoustic set by the Velvet Otters and Cork Valley taking the stage at 10:00 PM.

Hottest new bar in Frisco! Drink specials all night with the Zephyr Pale girls, and great live music to celebrate this grand opening.

I will use this for FB and other online marketing, as well as some print.

```html
<!DOCTYPE html>
<html lang="en">
<head>
<meta charset="utf-8">
<title>Quimby's Hall – Grand Opening</title>
<link href="https://fonts.googleapis.com/css2?family=PT+Sans+Narrow:wght@400;700&display=swap" rel="stylesheet">
<style>
  :root {
    --ink: #0b0908;
    --white: #ffffff;
    --yellow: #f7ef2a;
    --band: #1c1614;
    --red-deep: #7a0c0a;
    --red: #d8261a;
    --orange: #f08a1c;
    --olive: #4c4a36;
    --tape-blue: #a9dbe6;
    --tape-grey: #4a4a4a;
  }
  * { margin: 0; padding: 0; box-sizing: border-box; }
  html, body { width: 927px; height: 1200px; overflow: hidden; background: var(--ink); }
  .flyer {
    position: relative;
    width: 927px;
    height: 1200px;
    overflow: hidden;
    font-family: "PT Sans Narrow", "Arial Narrow", sans-serif;
    color: var(--white);
  }
  .backdrop {
    position: absolute; inset: 0;
    background:
      radial-gradient(ellipse 260px 220px at 700px 430px, rgba(255,240,60,.9), rgba(255,170,30,.4) 55%, transparent 80%),
      radial-gradient(ellipse 420px 300px at 480px 780px, rgba(240,110,20,.85), rgba(200,30,20,.55) 55%, transparent 85%),
      radial-gradient(ellipse 300px 380px at 260px 420px, rgba(140,20,15,.85), transparent 75%),
      radial-gradient(ellipse 360px 300px at 160px 160px, rgba(90,86,60,.9), transparent 80%),
      linear-gradient(180deg, #1a1612 0%, #120c0a 55%, #0a0707 100%);
  }
  .backdrop-floor {
    position: absolute; left: 0; right: 0; top: 965px; height: 50px;
    background: linear-gradient(180deg, rgba(0,0,0,.2), rgba(0,0,0,.7));
  }
  .headline, .pitch, .event, .venue { position: absolute; right: 41px; text-align: right; }
  .headline-top { top: 62px; font-size: 86px; font-weight: 700; line-height: 1; }
  .headline-sub { top: 160px; font-size: 54px; font-weight: 700; line-height: 1; }
  .pitch {
    top: 236px;
    color: var(--yellow);
    font-size: 38px; font-weight: 700; line-height: 50px;
    text-shadow: 2px 2px 0 #2a1a05, -1px -1px 0 #2a1a05;
  }
  .pitch-strong { font-size: 50px; line-height: 64px; }
  .date-band {
    position: absolute; left: 508px; right: 0; top: 578px; height: 46px;
    background: var(--band);
  }
  .date {
    position: absolute; right: 41px; top: 578px;
    color: var(--yellow); font-size: 38px; font-weight: 700; line-height: 46px;
  }
  .lineup {
    position: absolute; right: 41px; top: 634px; text-align: right;
    font-size: 27px; font-weight: 700; line-height: 34px;
    text-shadow: 1px 1px 0 #000;
  }
  .venue-logo {
    position: absolute; left: 36px; top: 370px;
    font-size: 98px; font-weight: 700; line-height: 92px;
    color: var(--white);
  }
  .player-frame {
    position: absolute; left: 128px; top: 705px; width: 232px; height: 250px;
    background: var(--white); padding: 10px;
    transform: rotate(6deg);
  }
  .player-photo {
    width: 100%; height: 100%;
    background: linear-gradient(160deg, #1d2c6a 0%, #3a4fae 45%, #8a2b3a 75%, #1a1a30 100%);
  }
  .band-mark {
    position: absolute; left: 46px; top: 1010px;
    display: flex; align-items: center; gap: 16px;
  }
  .band-mark-square { width: 64px; height: 64px; background: var(--tape-blue); border: 6px solid var(--tape-grey); }
  .band-mark-name { font-size: 40px; font-weight: 700; color: var(--white); }
  .venue-name { top: 980px; font-size: 56px; font-weight: 400; line-height: 1; }
  .venue-address { top: 1058px; font-size: 30px; line-height: 1; }
  .venue-phone { top: 1108px; font-size: 30px; line-height: 1; }
</style>
</head>
<body>
<main class="flyer">
  <div class="backdrop" role="img" aria-label="Red wine pouring into a glass over glowing party lights and a cheering crowd"></div>
  <div class="backdrop-floor"></div>

  <h1 class="headline headline-top">Hottest</h1>
  <h2 class="headline headline-sub">New Bar In Frisco!</h2>

  <p class="pitch">
    Drink specials all night<br>
    with the Zephyr Pale girls,<br>
    and great live music to<br>
    celebrate this<br>
    <span class="pitch-strong">grand opening.</span>
  </p>

  <div class="date-band"></div>
  <p class="date">Saturday April 5th.</p>
  <p class="lineup">
    Party starts at 7:00 PM with an acoustic<br>
    set by the Velvet Otters and Cork Valley<br>
    taking the stage at 10:00 PM.
  </p>

  <div class="venue-logo">Quimby's<br>Hall</div>

  <figure class="player-frame">
    <div class="player-photo" role="img" aria-label="Band bass player performing on stage under blue lights"></div>
  </figure>

  <div class="band-mark">
    <span class="band-mark-square"></span>
    <span class="band-mark-name">Cork Valley</span>
  </div>

  <p class="venue venue-name">Quimby's Hall</p>
  <p class="venue venue-address">8241 Larkspur Ave. #204, Frisco, Texas.</p>
  <p class="venue venue-phone">(214) 705-9183 for table reservations.</p>
</main>
</body>
</html>
```